Stylish WordPress Web Site for International Young Travellers and Families

We need a WordPress Website with a stylish design for our international online registration and matching solution for Au Pairs and Host Families called Nanny Lantern. We have strong competitors and wish to stand out with a straightforward registration process and fresh design. We need payment facilities and an easy navigation for Au Pairs and Host Families to log in, upload photos, edit their profiles etc. I need it well integrated and automation of payment receipts etc, and connected with PostFinch for newsletters etc. Logos supplied, along with website plan and text for pages. Some text to still be supplied. Can supply stock photos if required. Designer needs to advise. SIte needs to be translated into - French, Spanish, Italian, Dutch, German,

Target Market(s)

Young international travellors (aged 18-28 years) predominately female and Mums aged (28 - 48 years) of 2 or more children.

Industry/Entity Type

E-Commerce

Coding

Coded - Design and coding required

Font styles to use
Sans Serif

Requirements
Must have
• Simple registration. Great photos. Integrated with Post Finch. Payment facilities. Ease of log in for updating profiles, uploading photos etc. Site translated as listed above.
Nice to have
• Would love to see the compass design integrated throughout website.

```html
<!DOCTYPE html>
<html lang="en">
<head>
<meta charset="utf-8">
<title>Nanny Lantern — Au Pairs and Host Families</title>
<link href="https://fonts.googleapis.com/css2?family=Great+Vibes&family=Open+Sans:ital,wght@0,400;0,600;0,700;1,400&display=swap" rel="stylesheet">
<style>
:root{
  --navy:#4a4962;
  --navy-dark:#3d3c52;
  --sand:#b8ab86;
  --sand-dark:#a39670;
  --sand-light:#c9bc95;
  --sky:#5fa8da;
  --sky-light:#86bfe6;
  --ink:#555;
  --ink-soft:#777;
  --white:#fff;
  --paper:#f4f5f7;
  --footer-bar:#3a3a3c;
}
*{margin:0;padding:0;box-sizing:border-box}
html,body{width:1200px;height:3077px;overflow:hidden}
body{font-family:"Open Sans",Arial,sans-serif;color:var(--ink);background:var(--white);position:relative}
.abs{position:absolute}
.script{font-family:"Great Vibes",cursive}
section,header,footer{position:absolute;left:0;width:1200px;overflow:hidden}
.mark{display:inline-block;width:30px;height:30px;border:2px solid currentColor;border-radius:50%;vertical-align:middle;margin-right:12px}

/* header */
.site-header{top:0;height:130px;background:var(--white);z-index:3;overflow:visible}
.lang-select{left:868px;top:22px;width:136px;height:38px;border:1px solid #ccc;border-radius:3px;font-size:12px;line-height:36px;padding-left:34px;color:#444;background:#f3f3f3}
.lang-select::before{content:"";position:absolute;left:12px;top:13px;width:16px;height:11px;background:#2f4f9a}
.lang-select::after{content:"";position:absolute;right:14px;top:16px;border:5px solid transparent;border-top-color:#555}
.login-btn{left:1014px;top:20px;width:100px;height:40px;background:var(--navy);color:var(--white);border-radius:3px;font-size:14px;font-weight:600;line-height:40px;text-align:center}
.main-nav{left:430px;top:76px;width:770px;height:54px;background:var(--navy);display:flex;align-items:center}
.main-nav a{color:var(--white);text-decoration:none;font-size:12px;text-transform:uppercase;padding:0 22px;height:54px;line-height:54px;position:relative}
.main-nav a+a::before{content:"|";position:absolute;left:-2px;color:#aaa}
.main-nav a.current{background:var(--sand-light);padding:0 34px 0 44px;clip-path:polygon(26px 0,100% 0,100% 100%,0 100%)}
.brand{left:82px;top:-40px;width:272px;height:232px;background:var(--white);border-radius:50%;text-align:center;z-index:4}
.brand .mark{display:block;margin:72px auto 10px;color:var(--navy);width:34px;height:34px}
.brand-name{font-size:28px;font-weight:600;color:var(--navy)}

/* hero */
.hero{top:130px;height:481px}
.hero-photo{position:absolute;inset:0;background:linear-gradient(120deg,#5fb9c9 0%,#8ccad6 50%,#c6dcdb 100%)}
.hero-title{left:86px;top:150px;font-size:62px;color:var(--white);white-space:nowrap}
.hero-text{left:86px;top:232px;width:410px;font-size:12.5px;font-style:italic;line-height:24px;color:var(--white)}
.btn-dark{background:var(--navy);color:var(--white);font-size:13px;text-transform:uppercase;text-align:center}
.hero .btn-dark{left:86px;top:356px;width:146px;height:46px;line-height:46px}
.dots{left:556px;top:448px;display:flex;gap:6px}
.dots i{width:12px;height:12px;border:1px solid #fff;border-radius:50%}
.dots i.on{background:#555}

/* about */
.about{top:611px;height:343px;background:linear-gradient(90deg,var(--paper),#fff 60%,var(--paper))}
.about-art{left:70px;top:40px;width:290px;height:260px;border-radius:8px;background:linear-gradient(135deg,#e4e6ec,#cfd4df)}
.section-head{font-size:38px;color:#555;white-space:nowrap}
.section-head .accent{color:var(--sand-dark)}
.about .section-head{left:430px;top:40px}
.about .mark{color:#6a6a6a}
.about-copy{left:455px;top:100px;width:640px;font-size:12.5px;line-height:25px;color:var(--ink-soft)}
.about-copy p+p{margin-top:14px}

/* testimonials */
.testimonials{top:954px;height:437px;background:linear-gradient(180deg,var(--sand-light),var(--sand-dark))}
.center-head{left:0;width:1200px;text-align:center;color:var(--white)}
.testimonials .center-head{top:38px}
.quote{width:62px;height:62px;border-radius:50%;background:rgba(255,255,255,.35);color:var(--white);font-size:50px;line-height:78px;text-align:center;font-family:Georgia,serif}
.quote-text{width:440px;font-size:12px;font-style:italic;line-height:25px;text-align:center;color:var(--white)}
.avatar{width:84px;height:84px;border-radius:50%;border:4px solid rgba(255,255,255,.7);background:linear-gradient(160deg,#e8d7b4,#8fa7b8)}
.person{color:var(--white)}
.person .name{font-size:28px;line-height:32px;white-space:nowrap}
.person .role{font-size:12.5px;white-space:nowrap}

/* how it works */
.how{top:1391px;height:435px;background:linear-gradient(180deg,#6db0dd,var(--sky))}
.how .center-head{top:42px}
.step{top:130px;width:240px;margin-left:-120px;text-align:center;color:var(--white)}
.step-ring{width:116px;height:116px;margin:0 auto;border-radius:50%;border:2px solid rgba(255,255,255,.55);padding:9px}
.step-num{width:96px;height:96px;border-radius:50%;background:var(--white);color:#666;font-size:40px;font-style:italic;line-height:96px;font-weight:400}
.step .label{font-size:32px;margin-top:6px}
.step p{font-size:12px;font-style:italic;line-height:25px;margin-top:4px}

/* why */
.why{top:1826px;height:430px;background:var(--paper)}
.why .section-head{left:90px;top:42px;font-size:34px}
.why .mark{color:#6a6a6a}
.why-copy{left:86px;top:95px;width:500px;font-size:12.5px;line-height:25px;color:var(--ink-soft)}
.why-copy p+p{margin-top:14px}
.why .btn-dark{left:86px;top:348px;width:126px;height:38px;line-height:38px;font-size:12px}
.why-photo{left:632px;top:0;width:568px;height:430px;background:linear-gradient(135deg,#cdb37e,#8f8a55)}

/* members */
.members{top:2256px;height:482px}
.au-pairs{left:0;top:0;width:636px;height:482px;background:var(--sand)}
.hosts{left:636px;top:0;width:564px;height:482px;background:var(--navy)}
.panel-head{font-size:34px;color:var(--white);top:38px}
.au-pairs .panel-head{left:86px}
.hosts .panel-head{left:26px}
.country{font-size:12px;color:var(--white);display:flex;align-items:center;gap:10px}
.flag{width:26px;height:26px;border-radius:50%;flex:none}
.info-links{font-size:12px;color:var(--white);display:flex;flex-wrap:wrap;row-gap:18px}
.info-links span{display:flex;align-items:center;gap:6px;margin-right:30px}
.info-links span::before{content:"";width:9px;height:9px;border:2px solid var(--white);border-radius:50%}
.btn-outline{border:2px solid var(--white);color:var(--white);font-size:13px;text-transform:uppercase;text-align:center;height:38px;line-height:34px}
.hosts-copy{left:26px;top:90px;width:470px;font-size:12.5px;line-height:25px;color:var(--white)}
.lang-grid{left:26px;top:215px;width:470px;display:grid;grid-template-columns:repeat(3,1fr)}
.lang-grid .country{height:55px;border-bottom:1px solid rgba(255,255,255,.2)}
.lang-grid .flag{width:22px;height:22px}

/* footer */
.site-footer{top:2738px;height:273px;background:var(--sky);color:var(--white)}
.footer-brand{left:90px;top:60px;width:230px;text-align:center}
.footer-brand .mark{display:block;margin:0 auto 12px;width:40px;height:40px;color:var(--white)}
.footer-brand .brand-name{color:var(--white);font-size:30px}
.foot-head{font-size:14px;font-weight:700;text-transform:uppercase}
.contact{left:385px;top:42px}
.contact ul{list-style:none;margin-top:20px;font-size:11.5px}
.contact li{display:flex;gap:12px;align-items:flex-start;margin-bottom:13px}
.contact svg{flex:none}
.newsletter{left:632px;top:42px;width:215px}
.newsletter p,.follow p{font-size:11.5px;line-height:20px;margin-top:18px}
.email-field{margin-top:18px;height:32px;background:var(--white);color:#555;font-size:11.5px;line-height:32px;padding-left:10px}
.subscribe{margin-top:8px;width:80px;height:26px;background:var(--sand-light);font-size:10px;text-transform:uppercase;line-height:26px;text-align:center}
.follow{left:884px;top:42px;width:200px}
.social{display:flex;gap:10px;margin-top:18px}
.social i{width:34px;height:34px;border:2px solid var(--white);border-radius:50%}
.copyright{top:3011px;height:66px;background:var(--footer-bar);color:#ddd;font-size:12px;text-align:center;line-height:66px}
</style>
</head>
<body>

<header class="site-header">
  <div class="brand abs"><span class="mark"></span><span class="brand-name">Nanny Lantern</span></div>
  <div class="lang-select abs">English</div>
  <div class="login-btn abs">&#128274; LOGIN</div>
  <nav class="main-nav abs">
    <a class="current">Home</a><a>About us</a><a>How does it work?</a><a>Au Pairs</a><a>Host Family</a><a>Contact us</a>
  </nav>
</header>

<section class="hero">
  <div class="hero-photo" role="img" aria-label="Hero photo: family playing together on a sunny beach"></div>
  <h1 class="hero-title script abs">Nanny Lantern</h1>
  <p class="hero-text abs">Keeping your world and the little people in it happy, is no easy task. Sometimes that washing pile never gets smaller and wouldn't it be just great knowing that when you get home from work, that dinner is already on the be a more balanced, we all need a little help.</p>
  <div class="btn-dark abs">Read more</div>
  <div class="dots abs"><i></i><i></i><i class="on"></i><i></i><i></i></div>
</section>

<section class="about">
  <div class="about-art abs" role="img" aria-label="Decorative compass illustration"></div>
  <h2 class="section-head script abs"><span class="mark"></span>About <span class="accent">Nanny Lantern</span></h2>
  <div class="about-copy abs">
    <p>Keeping your world and the little people in it happy, is no easy task. Sometimes that washing pile never gets smaller and wouldn't it be just great knowing that when you get home from work, that dinner is already on the table, the kids fed, bathed and dressed for bed. We get it. Life is busy, a some time to get to the gym and maybe just to be a more balanced, we all need a little help.</p>
    <p>You can find your Nanny Lantern Au Pair, they are a person between the age of 18 and 30 years of age with various skills and experience to join you in your home. Often they are students taking a break from study to travel abroad. They are keen care for your children in exchange for full board and pocket money.</p>
  </div>
</section>

<section class="testimonials">
  <h2 class="center-head section-head script abs" style="color:#fff"><span class="mark"></span>Our Testimonials</h2>
  <div class="quote abs" style="left:300px;top:108px">&ldquo;</div>
  <div class="quote abs" style="left:840px;top:108px">&ldquo;</div>
  <p class="quote-text abs" style="left:105px;top:182px">I have been an Au Pair twice now, both with amazing families who have treated me like their daughter. The experience is unique and has given me the opportunity to travel affordably and practise my English. I love children and this is important, I love cooking and my families loved the meals I prepared. I would recommend for everyone to Au Pair it is the best!</p>
  <p class="quote-text abs" style="left:650px;top:182px">We have had 6 Au Pairs and each has become a member of our family and will be for life. The flexibility and convenience are great, I don't need to rush from work to daycare for pick ups and by having someone who knows and cares for your children well.</p>
  <div class="avatar abs" style="left:150px;top:326px" role="img" aria-label="Portrait of the au pair"></div>
  <div class="person abs" style="left:256px;top:340px"><div class="name script">Camille Duret - Au Pair</div><div class="role">(aged 20 years, from France)</div></div>
  <div class="avatar abs" style="left:690px;top:326px" role="img" aria-label="Portrait of the host mum"></div>
  <div class="person abs" style="left:796px;top:340px"><div class="name script">Rosalind Hale</div><div class="role">Host Mum, 3 children aged 18months to 8 years old</div></div>
</section>

<section class="how">
  <h2 class="center-head section-head script abs" style="color:#fff"><span class="mark"></span>How Does It Work</h2>
  <div class="step abs" style="left:207px"><div class="step-ring"><div class="step-num">01</div></div><div class="label script">Step</div><p>All that is required is a straightforward free registration and enter your search criteria and your ideal candidates profiles will be displayed.</p></div>
  <div class="step abs" style="left:468px"><div class="step-ring"><div class="step-num">02</div></div><div class="label script">Step</div><p>Once you have selected your choices you can send a secure message to discus details further including inter perfect Au Pair or Host Family.</p></div>
  <div class="step abs" style="left:726px"><div class="step-ring"><div class="step-num">03</div></div><div class="label script">Step</div><p>Au Pairs book their travel in and Host Families prepare to welcome you into their home.</p></div>
  <div class="step abs" style="left:985px"><div class="step-ring"><div class="step-num">04</div></div><div class="label script">Step</div><p>Once you have made your choice you can choose to make you profile inactive &amp; easily reinstate it again when you are being searching again.</p></div>
</section>

<section class="why">
  <h2 class="section-head script abs"><span class="mark"></span>Why <span class="accent">Nanny Lantern</span> is for you?</h2>
  <div class="why-copy abs">
    <p>We believe in the product – that's right you! Our founder said it well, "Do what you do so well that they will want to see it again and bring their friends." Creating love provide positive word of mouth and that's absolutely priceless.</p>
    <p>We know that our platform. It is the most modern and sophisticated and offers Au Pairs and Families the best solution and greatest of opportunities. We have experience – we are the Au Pairs and we are the experience ourselves of whats makes it benefits to both parties.</p>
  </div>
  <div class="btn-dark abs">Read more info</div>
  <div class="why-photo abs" role="img" aria-label="Photo: young traveller with a backpack looking over green hills"></div>
</section>

<section class="members">
  <div class="au-pairs abs">
    <h2 class="panel-head section-head script abs"><span class="mark"></span>Au Pairs</h2>
    <div class="abs" style="left:86px;top:96px;width:520px;display:grid;grid-template-columns:repeat(4,1fr);row-gap:24px">
      <div class="country"><i class="flag" role="img" aria-label="Flag" style="background:#3c5aa6"></i>America</div>
      <div class="country"><i class="flag" role="img" aria-label="Flag" style="background:#23408e"></i>Australia</div>
      <div class="country"><i class="flag" role="img" aria-label="Flag" style="background:#1f3b8a"></i>New Zealand</div>
      <div class="country"><i class="flag" role="img" aria-label="Flag" style="background:#d33a3a"></i>Austria</div>
      <div class="country"><i class="flag" role="img" aria-label="Flag" style="background:#e5b92c"></i>Belgium</div>
      <div class="country"><i class="flag" role="img" aria-label="Flag" style="background:#e03c3c"></i>Canada</div>
      <div class="country"><i class="flag" role="img" aria-label="Flag" style="background:#c8303a"></i>Denmark</div>
      <div class="country"><i class="flag" role="img" aria-label="Flag" style="background:#e9eef6"></i>Finland</div>
      <div class="country"><i class="flag" role="img" aria-label="Flag" style="background:#3553a4"></i>France</div>
      <div class="country"><i class="flag" role="img" aria-label="Flag" style="background:#d9a52a"></i>Germany</div>
      <div class="country"><i class="flag" role="img" aria-label="Flag" style="background:#2e4f9c"></i>Iceland</div>
      <div class="country"><i class="flag" role="img" aria-label="Flag" style="background:#3aa05a"></i>Ireland</div>
      <div class="country"><i class="flag" role="img" aria-label="Flag" style="background:#4aa45a"></i>Italy</div>
      <div class="country"><i class="flag" role="img" aria-label="Flag" style="background:#f1f1f1"></i>Japan</div>
      <div class="country"><i class="flag" role="img" aria-label="Flag" style="background:#3f9a55"></i>Mexico</div>
      <div class="country"><i class="flag" role="img" aria-label="Flag" style="background:#c64040"></i>Netherlands</div>
      <div class="country"><i class="flag" role="img" aria-label="Flag" style="background:#e6b330"></i>Spain</div>
      <div class="country"><i class="flag" role="img" aria-label="Flag" style="background:#2f6bb0"></i>Sweden</div>
      <div class="country"><i class="flag" role="img" aria-label="Flag" style="background:#d93838"></i>Switzerland</div>
      <div class="country"><i class="flag" role="img" aria-label="Flag" style="background:#2a3f86"></i>UK</div>
    </div>
    <div class="info-links abs" style="left:86px;top:362px;width:520px">
      <span>Placement periods</span><span>Duties</span><span>Pocket money</span><span>Board/lodging</span><span>Free time/holidays</span><span>Additional information</span>
    </div>
    <div class="btn-outline abs" style="left:90px;top:430px;width:112px">Sign up</div>
  </div>
  <div class="hosts abs">
    <h2 class="panel-head section-head script abs"><span class="mark"></span>Host Families</h2>
    <p class="hosts-copy abs">We know that our platform. It is the most modern and sophisticated and offers Au Pairs and Families the best solution and greatest of opportunities. We know that our platform. It is the most modern and sophisticated and offers Au Pairs and Families the best solution and greatest of opportunities.</p>
    <div class="lang-grid abs">
      <div class="country"><i class="flag" role="img" aria-label="Flag" style="background:#2a3f86"></i>English</div>
      <div class="country"><i class="flag" role="img" aria-label="Flag" style="background:#3553a4"></i>French</div>
      <div class="country"><i class="flag" role="img" aria-label="Flag" style="background:#e6b330"></i>Spanish</div>
      <div class="country"><i class="flag" role="img" aria-label="Flag" style="background:#4aa45a"></i>Italian</div>
      <div class="country"><i class="flag" role="img" aria-label="Flag" style="background:#c64040"></i>Dutch</div>
      <div class="country"><i class="flag" role="img" aria-label="Flag" style="background:#d9a52a"></i>German</div>
    </div>
    <div class="info-links abs" style="left:26px;top:346px;width:520px">
      <span>Placement periods</span><span>Duties</span><span>Pocket money</span><span>Board/lodging</span><span>Free time/holidays</span><span>Additional information</span>
    </div>
    <div class="btn-outline abs" style="left:54px;top:420px;width:100px">Sign up</div>
  </div>
</section>

<footer class="site-footer">
  <div class="footer-brand abs"><span class="mark"></span><span class="brand-name">Nanny Lantern</span></div>
  <div class="contact abs">
    <div class="foot-head">Contact us</div>
    <ul>
      <li><svg width="14" height="14" viewBox="0 0 14 14"><path d="M3 1h3l1 3-2 1.5a8 8 0 0 0 3.5 3.5L10 7l3 1v3a2 2 0 0 1-2 2A10 10 0 0 1 1 3a2 2 0 0 1 2-2z" fill="#fff"/></svg>(000)-121-1231 (Phone)</li>
      <li><svg width="14" height="14" viewBox="0 0 14 14"><rect x="3" y="1" width="8" height="4" fill="#fff"/><rect x="1" y="5" width="12" height="6" rx="1" fill="#fff"/><rect x="3" y="9" width="8" height="4" fill="#fff" stroke="#5fa8da"/></svg>(000)-121-1231 (Fax)</li>
      <li><svg width="14" height="14" viewBox="0 0 14 14"><rect x="1" y="3" width="12" height="8" fill="#fff"/><path d="M1 3l6 5 6-5" stroke="#5fa8da" fill="none"/></svg>info@nannylantern.com</li>
      <li><svg width="14" height="14" viewBox="0 0 14 14"><path d="M7 1a4 4 0 0 1 4 4c0 3-4 8-4 8S3 8 3 5a4 4 0 0 1 4-4z" fill="#fff"/><circle cx="7" cy="5" r="1.5" fill="#5fa8da"/></svg># 356 Lorem Ipsum Dummy<br>Lorem ipsum</li>
    </ul>
  </div>
  <div class="newsletter abs">
    <div class="foot-head">Newsletter</div>
    <p>Register Your email address to get information about us</p>
    <div class="email-field">Email Address</div>
    <div class="subscribe">Subscribe</div>
  </div>
  <div class="follow abs">
    <div class="foot-head">Follow us</div>
    <p>Lorem ipsum dolor sit amet, conse ctetur adipiscing elit. Nulla in purus nibh. Donec ornare</p>
    <div class="social" aria-label="Social links"><i></i><i></i><i></i><i></i><i></i></div>
  </div>
</footer>

<div class="copyright abs" style="left:0;width:1200px">© Copyright 2016 Nanny Lantern. All Rights Reserved</div>

</body>
</html>
```